Consultancy Business Card Design

We need a business card design for a new company based in singapore called FortyOne. FortyOne a boutique consultancy firm offering broad-based business solutions, from conception to re-invention, for ventures from new start-ups to long-running traditional businesses.
Its 2 main divisions (Food & Beverage Operations and Construction & Project Management) have access to a wide range of networks, knowledge bases, and resources to service its clients across numerous diverse sectors. This includes, and is not limited to, construction, F&B, and retail.
We are a company that combines the ambition, boldness and energy of one in the 20s with the dedication, level-headedness and dependability of one entering its 30s. Bridging the experiences of the old with ideals of the young, we draw on the positives of both to create a unique synergy.
We hope to see designs that fits our company profile.
Boutique
FortyOne(Company Name)
Marcus Leow (Name)
Principle Consultant (Title)
F&B and Hospitality (Division)
(+65) 8364 5170 (Contact no.)
marcus@fortyone-example.com.sg (Email)

```html
<!DOCTYPE html>
<html lang="en">
<head>
<meta charset="utf-8">
<title>FortyOne — Marcus Leow Business Card</title>
<link rel="stylesheet" href="https://fonts.googleapis.com/css2?family=Quicksand:wght@300;400;700&display=swap">
<style>
  :root {
    --card-bg: #0e1214;
    --accent: #5ad8f0;
    --decor-shade: #171b1d;
    --muted-text: #2a3235;
  }
  html, body {
    margin: 0;
    padding: 0;
    width: 1200px;
    height: 741px;
    overflow: hidden;
    background: var(--card-bg);
  }
  .card {
    position: relative;
    width: 1200px;
    height: 741px;
    background: var(--card-bg);
    font-family: "Quicksand", sans-serif;
    overflow: hidden;
  }
  .brand-decoration {
    position: absolute;
    left: 524px;
    top: 41px;
    width: 620px;
    height: 620px;
  }
  .identity {
    position: absolute;
    left: 132px;
    top: 244px;
    color: var(--accent);
  }
  .company-name {
    margin: 0 0 0 5px;
    font-size: 24px;
    font-weight: 400;
    letter-spacing: 3px;
    line-height: 26px;
  }
  .person-name {
    margin: 0;
    font-size: 52px;
    font-weight: 300;
    letter-spacing: 5px;
    line-height: 56px;
    white-space: nowrap;
  }
  .person-name .surname {
    font-weight: 700;
    letter-spacing: 4px;
  }
  .job-title {
    margin: 4px 0 0 0;
    font-size: 21px;
    font-weight: 400;
    letter-spacing: 3px;
    text-align: right;
    line-height: 24px;
  }
  .contact-list {
    position: relative;
    position: absolute;
    left: 88px;
    top: 548px;
    margin: 0;
    padding: 0;
    list-style: none;
    color: var(--muted-text);
    font-size: 27px;
    font-weight: 400;
    letter-spacing: 4px;
    line-height: 32.5px;
    white-space: nowrap;
  }
</style>
</head>
<body>
  <main class="card">
    <svg class="brand-decoration" role="img" aria-label="Large faint decorative brand circle" viewBox="0 0 620 620" xmlns="http://www.w3.org/2000/svg">
      <circle cx="310" cy="310" r="300" fill="var(--decor-shade)"/>
    </svg>

    <section class="identity">
      <p class="company-name">FortyOne</p>
      <h1 class="person-name">Marcus <span class="surname">Leow</span></h1>
      <p class="job-title">Principle Consultant</p>
    </section>

    <ul class="contact-list">
      <li>Division: F&amp;B and Hospitality</li>
      <li>Phone: (+65) 8364 5170</li>
      <li>Email: marcus@fortyone-example.com.sg</li>
    </ul>
  </main>
</body>
</html>
```